PRVD Traditional Business Card Project

Please see attached....just a simple business card... on attachment- please use the exact font, style, etc as the attached "Pat Everard Wynne" card... however, replace with the "Owen Reginald Talbot" text and address below the card.

```html
<!DOCTYPE html>
<html lang="en">
<head>
<meta charset="utf-8">
<title>PRVD Business Card – Owen Reginald Talbot</title>
<link rel="stylesheet" href="https://fonts.googleapis.com/css2?family=Old+Standard+TT:wght@400;700&family=Questrial&display=swap">
<style>
  :root {
    --backdrop: #5f5f5f;
    --card: #ffffff;
    --ink: #1b1b1b;
    --ink-soft: #3a3a3a;
    --rule: #8a8a8a;
  }
  * { margin: 0; padding: 0; box-sizing: border-box; }
  html, body {
    width: 1200px; height: 1200px; overflow: hidden;
    background: var(--backdrop);
  }
  .card {
    position: absolute;
    left: 75px; top: 300px;
    width: 1050px; height: 599px;
    background: var(--card);
    color: var(--ink);
  }
  .firm {
    position: absolute;
    right: 46px; top: 52px;
    text-align: center;
    font-family: "Old Standard TT", serif;
  }
  .firm-name {
    font-size: 40px;
    font-weight: 400;
    font-variant: small-caps;
    letter-spacing: 1px;
    line-height: 1.2;
  }
  .firm-sub {
    font-size: 17px;
    font-weight: 700;
    letter-spacing: 1.2px;
    color: var(--ink-soft);
    margin-top: 4px;
  }
  .person {
    position: absolute;
    left: 51px; top: 252px;
  }
  .person-name {
    font-family: "Old Standard TT", serif;
    font-weight: 700;
    font-size: 30px;
    letter-spacing: 0.5px;
    text-transform: uppercase;
  }
  .person-title {
    font-family: "Questrial", sans-serif;
    font-size: 23px;
    color: var(--ink-soft);
    margin-top: 14px;
    letter-spacing: 0.5px;
  }
  .divider {
    position: absolute;
    left: 51px; right: 48px; top: 370px;
    height: 2px;
    background: var(--rule);
  }
  .contacts {
    position: absolute;
    left: 51px; top: 400px;
    list-style: none;
    font-family: "Questrial", sans-serif;
    font-size: 21px;
    letter-spacing: 1.6px;
    color: var(--ink-soft);
  }
  .contacts li {
    display: flex; align-items: center;
    height: 40px;
  }
  .contacts .caps { font-variant: small-caps; text-transform: lowercase; font-size: 24px; }
  .contact-icon { width: 19px; height: 19px; margin-right: 12px; flex: none; }
  .address {
    position: absolute;
    right: 46px; top: 481px;
    text-align: right;
    font-family: "Questrial", sans-serif;
    font-size: 22px;
    letter-spacing: 2px;
    line-height: 37px;
    color: var(--ink-soft);
    text-transform: uppercase;
  }
</style>
</head>
<body>
  <div class="card">
    <div class="firm">
      <div class="firm-name">Pacific Ridge Valley</div>
      <div class="firm-sub">DEFENDERS GROUP, PLC</div>
    </div>

    <div class="person">
      <div class="person-name">Owen Reginald Talbot</div>
      <div class="person-title">ATTORNEY AT LAW</div>
    </div>

    <div class="divider"></div>

    <ul class="contacts">
      <li>
        <svg class="contact-icon" viewBox="0 0 20 20" aria-label="Phone"><circle cx="10" cy="10" r="10" fill="#1b1b1b"/><path d="M6.5 5.2l2 .1.8 2.4-1.3 1a6 6 0 0 0 3.3 3.3l1-1.3 2.4.8.1 2a1 1 0 0 1-1.1 1A9 9 0 0 1 5.5 6.3a1 1 0 0 1 1-1.1z" fill="#fff"/></svg>
        <span>(555) 214-3800</span>
      </li>
      <li>
        <svg class="contact-icon" viewBox="0 0 20 20" aria-label="Fax"><circle cx="10" cy="10" r="10" fill="#1b1b1b"/><rect x="7" y="4.5" width="6" height="3" fill="#fff"/><rect x="5" y="8" width="10" height="5" rx="1" fill="#fff"/><rect x="7" y="11.5" width="6" height="4" fill="#fff" stroke="#1b1b1b" stroke-width=".8"/></svg>
        <span>(555) 214-3801</span>
      </li>
      <li>
        <svg class="contact-icon" viewBox="0 0 20 20" aria-label="Email"><circle cx="10" cy="10" r="10" fill="#1b1b1b"/><rect x="5" y="6.5" width="10" height="7" fill="#fff"/><path d="M5 6.8l5 3.8 5-3.8" fill="none" stroke="#1b1b1b" stroke-width="1"/></svg>
        <span class="caps">otalbot@lawprvd.com</span>
      </li>
      <li>
        <svg class="contact-icon" viewBox="0 0 20 20" aria-label="Website"><circle cx="10" cy="10" r="10" fill="#1b1b1b"/><circle cx="10" cy="10" r="5" fill="none" stroke="#fff" stroke-width="1.2"/><ellipse cx="10" cy="10" rx="2.2" ry="5" fill="none" stroke="#fff" stroke-width="1"/><path d="M5 10h10" stroke="#fff" stroke-width="1"/></svg>
        <span class="caps">www.lawprvd.com</span>
      </li>
    </ul>

    <address class="address" style="font-style:normal">
      2740 Cedar Lane, Suite B<br>
      Alder Springs, CA 91999
    </address>
  </div>
</body>
</html>
```